I have done a draft (as attached) but also want to add the following "profile story" of the type of customers we are seeking. We are open to colours and layout so go for it!
Gest Profile: “Come and Stay” at Corvell Ridge Holiday Park
Dennis and Fay Mortlock from Victoria are soaking up the sun at Corvell Ridge taking advantage of our special “Come and Stay” rate.
Each year, Dennis and Fay leave their family home, kids and grandkids behind and spend some time away together in their caravan in the warmer climate of Corvell Heads.
Dennis says “We used to stay at many different parks for two or three days at a time before moving on, but that was just too much work. So we decided to look at the map and pick somewhere we could stay for a month or more. The map showed that Ridge is surrounded by beautiful waterways, so we decided to see what was on offer for a longer stay.”
Now this year is their fourth stay with us and they have already booked for next year – same site, same dates! Dennis says “this site is my favourite and so the park makes it available for us each year.”
Park Manager Warren Tibbet advises that this is something they do for regular Christmas and Easter campers as well. “It makes it easy for people to plan their stay and they enjoy the familiarity of securing the same site”.
We offer a special invitation rate for people just like Dennis and Fay. It’s called the “Come and Stay” rate and is usually offered to new guests when rebooking for the following year during the winter months. It is based on stays of a month or more and is now also available in the pet friendly section.
Manager Warren says “the “Come and Stay” pricing works out to about $25.00 a night, which is a very good discount of about $11.00 a night! There are special conditions like a minimum stay periods and it is only for tourists just like Dennis and Fay but it certainly makes it affordable to escape the winter weather each year!”
If you are looking for a place to base yourself as a tourist for a month or more contact Corvell Ridge 02 6617 4082 and secure next years winter escape. You might even end up next to Dennis and Fay!
Retirees.
Pet
Designer to choose colors to be used in the design.

```html
<!DOCTYPE html>
<html lang="en">
<head>
<meta charset="utf-8">
<title>Come &amp; Stay – Corvell Ridge Holiday Park</title>
<link href="https://fonts.googleapis.com/css2?family=Arimo:wght@400;700&family=Pinyon+Script&family=Kalam:wght@400&family=Tinos&display=swap" rel="stylesheet">
<style>
  :root {
    --sun: #fcc97a;
    --pink: #e0306f;
    --pink-dark: #3a1020;
    --cream: #fdeec4;
    --sky: #8ed4f2;
    --navy: #3a3f9a;
    --ink: #222;
    --white: #fff;
    --orange: #f08a1e;
  }
  * { box-sizing: border-box; margin: 0; padding: 0; }
  html, body { width: 900px; height: 1200px; overflow: hidden; }
  body { background: var(--sun); font-family: "Arimo", Arial, sans-serif; color: var(--ink); position: relative; }

  .masthead {
    position: absolute; left: 4px; top: 4px; width: 688px; height: 184px;
    background: var(--pink); border-bottom-right-radius: 80px; border-top-right-radius: 24px;
  }
  .masthead__eyebrow {
    position: absolute; left: 132px; top: 12px; font-family: "Pinyon Script", cursive;
    font-size: 32px; color: var(--white);
  }
  .masthead__title {
    position: absolute; left: 30px; top: 58px; font-size: 95px; color: var(--white);
    font-weight: 400; line-height: 1; white-space: nowrap;
  }

  .brand {
    position: absolute; left: 708px; top: 10px; width: 140px; height: 142px;
    background: var(--white); display: flex; flex-direction: column;
    align-items: center; justify-content: center; gap: 8px;
  }
  .brand__dot { width: 18px; height: 18px; border-radius: 50%; background: var(--navy); }
  .brand__name { font-size: 19px; color: var(--navy); text-align: center; line-height: 1.15; }

  .offer {
    position: absolute; left: 4px; top: 192px; width: 326px; height: 340px; background: var(--sun);
    border-right: 3px solid var(--white); border-bottom: 3px solid var(--white);
  }
  .offer__lead { position: absolute; left: 14px; top: 44px; width: 292px; font-size: 20px; line-height: 1.3; }
  .offer__price { position: absolute; left: 18px; top: 184px; width: 285px; font-size: 21px; font-weight: 700; line-height: 1.4; }
  .offer__price span { font-size: 18px; }

  .hero-photo {
    position: absolute; left: 330px; top: 162px; width: 567px; height: 336px; z-index: 1;
    background: linear-gradient(160deg, #3a3a2c 0%, #8b7a55 40%, #e9c78a 62%, #6b6a48 100%);
  }

  .rates {
    position: absolute; left: 504px; top: 498px; width: 390px; height: 160px; z-index: 2;
    background: var(--sky); border: 3px solid var(--white); border-bottom-left-radius: 40px;
    border-top-left-radius: 8px;
  }
  .rates__title { position: absolute; left: 24px; top: 10px; font-size: 25px; font-weight: 400; color: var(--pink); line-height: 1.25; }
  .rates__rule { position: absolute; left: 16px; top: 73px; width: 362px; height: 5px; background: var(--navy); }
  .rates__list { position: absolute; left: 26px; top: 94px; font-size: 20.5px; line-height: 1.25; list-style: none; white-space: nowrap; }

  .profile {
    position: absolute; left: 4px; top: 540px; width: 480px; height: 296px; background: var(--white);
  }
  .profile__intro { position: absolute; left: 26px; top: 6px; width: 390px; font-size: 14px; font-weight: 700; line-height: 1.25; }
  .profile__photo {
    position: absolute; left: 21px; top: 72px; width: 358px; height: 210px;
    background: linear-gradient(180deg, #2f7bd6 0%, #7fb4de 32%, #e8eef2 50%, #7a9a4a 80%, #5e7f36 100%);
  }

  .story {
    position: absolute; left: 4px; top: 838px; width: 479px; height: 356px;
    background: var(--cream); padding: 5px 18px 0 18px; font-size: 9.6px; line-height: 1.27;
  }
  .story p { margin-bottom: 9px; }

  .tagline {
    position: absolute; left: 484px; top: 708px; width: 406px; height: 54px; background: var(--white);
    font-family: "Kalam", cursive; color: var(--orange);
    font-size: 29px; text-align: center; line-height: 58px;
  }

  .contact {
    position: absolute; left: 528px; top: 797px; width: 352px; height: 384px; background: var(--pink);
    border-radius: 22px; border-top-left-radius: 34px; box-shadow: 8px 8px 0 var(--sky);
    color: var(--white); border: 3px solid var(--white);
  }
  .contact__lead { position: absolute; left: 22px; top: 28px; width: 310px; font-size: 13.5px; font-weight: 700; color: var(--pink-dark); line-height: 1.2; }
  .contact__name { position: absolute; left: 38px; top: 76px; font-size: 22px; line-height: 1.6; }
  .contact__name span { display: block; padding-left: 28px; }
  .contact__details { position: absolute; left: 24px; top: 150px; font-family: "Tinos", serif; font-size: 24px; line-height: 1.3; white-space: nowrap; }
  .contact__web { position: absolute; left: 30px; top: 266px; font-family: "Tinos", serif; font-size: 20px; }
  .contact__cta { position: absolute; left: 50px; top: 308px; font-size: 13px; }
  .contact__close { position: absolute; left: 20px; top: 340px; font-size: 13px; font-weight: 700; }
</style>
</head>
<body>
  <header class="masthead">
    <div class="masthead__eyebrow">Special Invitation</div>
    <h1 class="masthead__title">Come &amp; Stay</h1>
  </header>

  <div class="brand">
    <div class="brand__dot"></div>
    <div class="brand__name">Corvell Ridge<br>holiday park</div>
  </div>

  <section class="offer">
    <p class="offer__lead">Enjoy Special rates offers for valued clients for a minimum 28&#8209;night stay during Winter.</p>
    <p class="offer__price">Escape the cold southern weather for as low as $25.00 <span>per night!!!</span></p>
  </section>

  <div class="hero-photo" role="img" aria-label="Caravan with awning on a powered site at sunset beside the water"></div>

  <section class="rates">
    <h2 class="rates__title">Discounted Powered &amp;<br>Ensuites Sites</h2>
    <div class="rates__rule"></div>
    <ul class="rates__list">
      <li>Powered Site..................$175 p/w</li>
      <li>Ensuite Powered Site......$210 p/w</li>
    </ul>
  </section>

  <section class="profile">
    <p class="profile__intro">Dennis and Fay Mortlock from Victoria are soaking up the sun at Corvell Ridge taking advantage of our special “Come and Stay” rate.</p>
    <div class="profile__photo" role="img" aria-label="Retired couple seated on camp chairs under their caravan awning"></div>
  </section>

  <article class="story">
    <p>Each year, Dennis and Fay leave their family home, kids and grandkids behind and spend some time away together in their caravan in the warmer climate of Corvell Heads.</p>
    <p>Dennis says “We used to stay at many different parks for two or three days at a time before moving on, but that was just too much work. So we decided to look at the map and pick somewhere we could stay for a month or more. The map showed that Ridge is surrounded by beautiful waterways, so we decided to see what was on offer for a longer stay.”</p>
    <p>Now this year is their fourth stay with us and they have already booked for next year – same site, same dates! Dennis says “this site is my favourite and so the park makes it available for us each year.”</p>
    <p>Park Manager Warren Tibbet advises that this is something they do for regular Christmas and Easter campers as well. “It makes it easy for people to plan their stay and they enjoy the familiarity of securing the same site”.</p>
    <p>We offer a special invitation rate for people just like Dennis and Fay. It’s called the “Come and Stay” rate and is usually offered to new guests when rebooking for the following year during the winter months. It is based on stays of a month or more and is now also available in the pet friendly section.</p>
    <p>Manager Warren says “the “Come and Stay” pricing works out to about $25.00 a night, which is a very good discount of about $11.00 a night! There are special conditions like a minimum stay periods and it is only for tourists just like Dennis and Fay but it certainly makes it affordable to escape the winter weather each year!”</p>
    <p>If you are looking for a place to base yourself as a tourist for a month or more contact Corvell Ridge 02 6617 4082 and secure next years winter escape.<br>You might even end up next to Dennis and Fay!</p>
  </article>

  <div class="tagline">Australia’s Best Get-away</div>

  <aside class="contact">
    <p class="contact__lead">If you are looking for a place to base yourself as a tourist for a month or more contact:</p>
    <p class="contact__name">CORVELL RIDGE<span>HOLIDAY PARK</span></p>
    <p class="contact__details">14 Harlow Dr Corvell Heads<br>NSW 2999<br>(02) 6617 4082</p>
    <p class="contact__web">www.corvellridge.com.au</p>
    <p class="contact__cta">...and secure next years winter escape.</p>
    <p class="contact__close">You might even end up next to Dennis and Fay!</p>
  </aside>
</body>
</html>
```